Simple elegant business card

General card for a fin and television director.
Just want name, email, phone and address.

Target Market(s)

Prospective employers

Industry/Entity Type

Business

Requirements
Must have
• As above
Nice to have
• Logo but not necessary.
Should not have
• Not too colourful or funky.
• Simplicity and elegance the way to go.

```html
<!DOCTYPE html>
<html lang="en">
<head>
<meta charset="UTF-8">
<title>Lena Hartley — Business Card</title>
<link rel="stylesheet" href="https://fonts.googleapis.com/css2?family=Inter:wght@300;400&display=swap">
<style>
  :root {
    --panel-top: #242424;
    --panel-bottom: #1d1d1d;
    --stage-dark: #0f0f0f;
    --stage-mid: #2c2c2c;
    --spotlight: #6e6e6e;
    --gold: #c99a30;
    --ink: #ffffff;
  }
  html, body {
    margin: 0;
    padding: 0;
    overflow: hidden;
    background: var(--stage-dark);
  }
  .card {
    position: relative;
    width: 1200px;
    height: 668px;
    overflow: hidden;
    font-family: "Inter", "Helvetica Neue", Arial, sans-serif;
    background:
      radial-gradient(ellipse 520px 240px at 600px 668px, var(--spotlight) 0%, #4a4a4a 35%, var(--stage-mid) 65%, var(--stage-dark) 100%);
  }
  .card__panel {
    position: absolute;
    left: 0;
    top: 0;
    width: 1200px;
    height: 440px;
    background: linear-gradient(180deg, var(--panel-top), var(--panel-bottom));
    box-shadow: 0 24px 50px 10px rgba(0, 0, 0, 0.95);
  }
  .card__name {
    position: absolute;
    top: 110px;
    left: 0;
    width: 100%;
    margin: 0;
    text-align: center;
    font-weight: 300;
    font-size: 68px;
    letter-spacing: 0.5px;
    color: var(--gold);
  }
  .card__contact {
    position: absolute;
    top: 238px;
    left: 0;
    width: 100%;
    margin: 0;
    text-align: center;
    font-weight: 300;
    font-size: 42px;
    line-height: 50px;
    color: var(--ink);
  }
  .card__contact span {
    display: block;
  }
</style>
</head>
<body>
  <div class="card">
    <section class="card__panel">
      <h1 class="card__name">Lena Hartley</h1>
      <p class="card__contact">
        <span class="card__email">lenahartley@reel.tv</span>
        <span class="card__phone">+1 310 555 0148</span>
        <span class="card__address">1420 Sunset Blvd, Los Angeles, CA</span>
      </p>
    </section>
  </div>
</body>
</html>
```